Your complete Gardening and lawn maintenance, Horticultural care. (to be on card)
We are looking at using a logo of a tree, with a recycling emblem circling the tree. The colors of choice, are burnt oranges and olive greens. Presented; simple to the eye, yet catchy to the clients in a eco-friendly way. We have uploaded a design for you to look at just to give a rough idea, you can use that or create your own ideas or play around with a mixture.

Target Market(s)

Home owners, businesses, real estates.

Industry/Entity Type

Recycling

Contact Information for Business Card

Name: Colin Breversted
Phone: 0438159027
Email: brightmossyards@mailbarn.net

Logo Text

Bright-Moss Yards

Logo styles of interest
Emblem Logo
Pictorial/Combination Logo
Abstract Logo
Requirements
Must have
• Business name: Bright-Moss Yards
and slogan : Your complete Gardening and lawn maintenance, Horticultural care

```html
<!DOCTYPE html>
<html lang="en">
<head>
<meta charset="utf-8">
<title>Bright-Moss Yards – Business Card</title>
<link rel="stylesheet" href="https://fonts.googleapis.com/css2?family=Open+Sans:wght@400;600;700&display=swap">
<style>
  :root {
    --olive: #6b7a2a;
    --olive-faint: #e8e6dc;
    --burnt-orange: #d4581f;
    --phone-grey: #6f7256;
    --card: #ffffff;
    --backdrop: #e9eaec;
    --shadow: rgba(30, 35, 45, 0.18);
  }
  * { box-sizing: border-box; margin: 0; padding: 0; }
  html, body {
    width: 1200px; height: 900px; overflow: hidden;
    background: var(--backdrop);
    font-family: "Open Sans", sans-serif;
  }
  .canvas { position: relative; width: 1200px; height: 900px; }

  .card {
    position: absolute;
    background: var(--card);
    box-shadow: 0 10px 30px var(--shadow);
    overflow: hidden;
  }

  /* Back: contact side, portrait */
  .card-back { left: 150px; top: 170px; width: 320px; height: 560px; }
  .contact-name {
    position: absolute; left: 40px; top: 56px;
    color: var(--olive); font-size: 30px; line-height: 1.1;
  }
  .contact-name::before {
    content: ""; display: block; width: 70px; height: 2px;
    background: var(--burnt-orange); margin-bottom: 12px;
  }
  .contact-name .given { font-weight: 400; display: block; }
  .contact-name .family { font-weight: 700; display: block; }
  .faint-circle { position: absolute; left: 60px; top: 200px; }
  .contact-phone {
    position: absolute; right: 44px; top: 230px;
    text-align: right; color: var(--phone-grey);
    font-size: 46px; font-weight: 400; line-height: 1.15;
  }
  .contact-email {
    position: absolute; left: 0; right: 0; bottom: 40px;
    text-align: center; color: var(--burnt-orange); font-size: 13px;
  }

  /* Front: brand side, landscape */
  .card-front { left: 540px; top: 310px; width: 560px; height: 320px; }
  .brand {
    position: absolute; left: 70px; top: 100px;
    display: flex; align-items: center; gap: 18px;
  }
  .brand-name {
    color: var(--olive); font-size: 38px; font-weight: 700; letter-spacing: -0.5px;
  }
  .slogan-band {
    position: absolute; left: 0; right: 0; bottom: 0; height: 52px;
    background: var(--burnt-orange);
    display: flex; align-items: center; justify-content: center;
  }
  .slogan { color: #fff; font-size: 15.5px; font-weight: 400; }
</style>
</head>
<body>
<main class="canvas">
  <section class="card card-back" aria-label="Contact side">
    <h2 class="contact-name"><span class="given">Colin</span><span class="family">Breversted</span></h2>
    <svg class="faint-circle" width="200" height="200" viewBox="0 0 200 200" aria-hidden="true">
      <circle cx="100" cy="100" r="90" fill="none" stroke="var(--olive-faint)" stroke-width="8"/>
    </svg>
    <p class="contact-phone">+0<br>43815<br>9027</p>
    <p class="contact-email">brightmossyards@mailbarn.net</p>
  </section>

  <section class="card card-front" aria-label="Brand side">
    <div class="brand">
      <h1 class="brand-name">Bright-Moss Yards</h1>
      <svg width="54" height="54" viewBox="0 0 54 54" aria-hidden="true">
        <circle cx="27" cy="27" r="23" fill="none" stroke="var(--olive)" stroke-width="5"/>
      </svg>
    </div>
    <div class="slogan-band">
      <p class="slogan">Your complete Gardening and lawn maintenance, Horticultural care</p>
    </div>
  </section>
</main>
</body>
</html>
```